Vex9Tax Business Card

Need a new business card for my law firm. The major components for the card will be my logo "Vex9Tax," the photo of me, contact information, and a QR Code for my website vex9tax.com. If you are unable to generate a QR Code, let me know and I'll see if I can make one. For the "Vex9Tax" logo, don't worry about the "Ride The Wave" part, you can leave that out. Here are my and the firm details:
Benedicto R Salazar III
Attorney at Law
Address: 250 Harbor Plaza, Suite 400
Dallas, TX 75201
Office #: 877-482-6173
Cell #: 214-657-3381
Fax #: 469-738-5126
Email: vex@vex9tax.com
Website: vex9tax.com

```html
<!DOCTYPE html>
<html lang="en">
<head>
<meta charset="utf-8">
<title>Vex9Tax Business Card</title>
<link href="https://fonts.googleapis.com/css2?family=Montserrat:wght@300;400;600;700;800&display=swap" rel="stylesheet">
<style>
  :root {
    --bg: #f2f2f2;
    --card-white: #f4f5f5;
    --brand-blue: #38b6e2;
    --brand-blue-light: #42c4e8;
    --faint-blue: #d6e8ef;
    --photo-tone-top: #c9d3d9;
    --photo-tone-bottom: #9fb0ba;
    --ink: #1d1d1f;
    --ink-soft: #555a5e;
    --white: #ffffff;
  }
  * { box-sizing: border-box; margin: 0; padding: 0; }
  html, body { width: 1200px; height: 800px; overflow: hidden; }
  body {
    background: var(--bg);
    font-family: "Montserrat", sans-serif;
    position: relative;
  }
  .card {
    position: absolute;
    top: 252px;
    width: 520px;
    height: 297px;
    border-radius: 2px;
    overflow: hidden;
    box-shadow: 0 2px 10px rgba(0,0,0,0.08);
  }
  .card--front { left: 45px; background: var(--card-white); }
  .card--back {
    left: 635px;
    background: linear-gradient(120deg, var(--brand-blue), var(--brand-blue-light));
  }

  .front__block {
    position: absolute; right: 70px; bottom: -40px;
    width: 150px; height: 130px;
    background: var(--faint-blue);
  }
  .front__header { position: absolute; left: 30px; top: 28px; display: flex; gap: 10px; }
  .front__marker { width: 11px; height: 16px; background: var(--brand-blue); margin-top: 1px; }
  .front__name {
    font-weight: 700; font-size: 14px; color: var(--ink);
    text-transform: uppercase; letter-spacing: 0.3px;
  }
  .front__title {
    font-weight: 300; font-size: 10px; color: var(--ink-soft);
    text-transform: uppercase; margin-top: 2px;
  }
  .front__photo {
    position: absolute; right: 30px; top: 28px;
    width: 84px; height: 100px;
    background: linear-gradient(180deg, var(--photo-tone-top), var(--photo-tone-bottom));
  }
  .front__contact {
    position: absolute; left: 30px; top: 108px;
    font-size: 11px; font-weight: 400; color: var(--ink-soft); line-height: 1.5;
  }
  .front__address { margin-bottom: 6px; }
  .contact-list { list-style: none; }
  .contact-list li { display: flex; align-items: center; gap: 7px; line-height: 1.55; }
  .contact-list svg { width: 9px; height: 9px; fill: var(--brand-blue); flex: none; }

  .front__brand {
    position: absolute; right: 30px; top: 142px;
    display: flex; align-items: center; gap: 8px;
  }
  .brand-square { width: 12px; height: 12px; background: var(--brand-blue); }
  .brand-name {
    font-weight: 800; font-size: 26px; color: var(--ink); letter-spacing: 0.5px;
  }

  .back__name {
    position: absolute; left: 0; right: 0; top: 118px;
    text-align: center;
    font-weight: 800; font-size: 44px; line-height: 1; color: var(--white); letter-spacing: 1px;
  }
  .back__qr {
    position: absolute; right: 24px; bottom: 24px;
    width: 64px; height: 64px;
    background: var(--white);
    border-radius: 3px;
  }
</style>
</head>
<body>
  <section class="card card--front">
    <div class="front__block"></div>
    <header class="front__header">
      <span class="front__marker"></span>
      <div>
        <h1 class="front__name">Benedicto R Salazar III</h1>
        <p class="front__title">Attorney at Law</p>
      </div>
    </header>
    <div class="front__photo" role="img" aria-label="Portrait photo of Benedicto R Salazar III"></div>
    <div class="front__contact">
      <p class="front__address">250 Harbor Plaza, Suite 400<br>Dallas, TX 75201</p>
      <ul class="contact-list">
        <li><svg viewBox="0 0 10 10"><path d="M1 2.5C1 1.5 2 1 5 1s4 .5 4 1.5V4H7V3H3v1H1z M2 5h6l1 4H1z"/></svg>877-482-6173</li>
        <li><svg viewBox="0 0 10 10"><path d="M2 0.5C1.5 0.5 1 1 1.5 2.5 2.5 6 4 7.8 7.5 8.8 9 9.2 9.5 8.5 9.5 8L8 6.5 6.5 7.3C5 6.5 3.5 5 2.7 3.5L3.5 2z"/></svg>214-657-3381</li>
        <li><svg viewBox="0 0 10 10"><path d="M2.5 0.5h4v3h-4z M1 4h8v4.5H1z M2.5 7h5v2.5h-5z"/></svg>469-738-5126</li>
        <li><svg viewBox="0 0 10 10"><path d="M0.5 2h9v6h-9z M1 2.5 5 5.5 9 2.5" stroke="#fff" stroke-width="0.8"/></svg>vex@vex9tax.com</li>
        <li><svg viewBox="0 0 10 10"><circle cx="5" cy="5" r="4.5"/><path d="M0.5 5h9M5 0.5c-2 2-2 7 0 9M5 0.5c2 2 2 7 0 9" stroke="#fff" stroke-width="0.7" fill="none"/></svg>vex9tax.com</li>
      </ul>
    </div>
    <div class="front__brand">
      <span class="brand-square"></span>
      <span class="brand-name">Vex9Tax</span>
    </div>
  </section>

  <section class="card card--back">
    <p class="back__name">Vex9Tax</p>
    <div class="back__qr" role="img" aria-label="QR code linking to vex9tax.com"></div>
  </section>
</body>
</html>
```